Brantley Lawn Care. The best in the biz

I run a lawn care service that offers full service mowing. 100% satisfaction guarantee. Fast, Friendly, quality service "I am your lawns best friend" I cut residential lawns. I offer a mow package that includes trimming, edging and clean up. Prices very from 20 dollars to 75. I want my logo to stand out. Free estimates

Target Market(s)

Home owners

Industry/Entity Type

Landscaping

Contact Information for Business Card

555-612-4470 tidymow47@quillmail.example Dexter. Brantley Lawn care

Colors
f37122
9bcb3c
cadf82

Requirements
Must have
• Company name.
• Phone number
• Email
• My services
• images
Nice to have
• A sun that is growing grass.
Should not have
• Incorrect information

```html
<!DOCTYPE html>
<html lang="en">
<head>
<meta charset="utf-8">
<title>Brantley Lawn Care – Business Card</title>
<link rel="stylesheet" href="https://fonts.googleapis.com/css2?family=Crimson+Text:wght@400&family=Open+Sans:wght@400&display=swap">
<style>
  :root {
    --backdrop: #e9e6df;
    --card: #ffffff;
    --ink: #2b2b2b;
    --ink-soft: #6e6e6e;
    --sun: #f37122;
    --brand-green: #2f7a2a;
  }
  html, body {
    margin: 0;
    width: 1200px;
    height: 1023px;
    overflow: hidden;
    background: var(--backdrop);
  }
  .business-card {
    position: absolute;
    left: 75px;
    top: 211px;
    width: 1050px;
    height: 600px;
    background: var(--card);
    overflow: hidden;
    box-shadow: 0 6px 18px rgba(0,0,0,0.18);
  }
  .grass-field {
    position: absolute;
    inset: 0;
    width: 1050px;
    height: 600px;
  }
  .brand {
    position: absolute;
    left: 36px;
    top: 150px;
    display: flex;
    align-items: center;
    gap: 12px;
  }
  .brand-dot {
    width: 44px;
    height: 44px;
    border-radius: 50%;
    background: var(--sun);
    flex: none;
  }
  .brand-name {
    font-family: "Crimson Text", Georgia, serif;
    font-size: 26px;
    color: var(--brand-green);
    line-height: 1;
    white-space: nowrap;
  }
  .contact {
    position: absolute;
    left: 340px;
    top: 62px;
    font-family: "Crimson Text", Georgia, serif;
    color: var(--ink);
  }
  .contact-name {
    font-size: 48px;
    margin: 0 0 4px;
    line-height: 1.05;
    font-weight: 400;
    white-space: nowrap;
  }
  .contact-role,
  .contact-line {
    margin: 0;
    font-size: 26px;
    line-height: 1.2;
    color: var(--ink-soft);
    white-space: nowrap;
  }
  .service-bar {
    position: absolute;
    top: 500px;
    height: 46px;
    border-radius: 23px;
    background: rgba(255,255,255,0.94);
    box-shadow: 0 0 10px 6px rgba(255,255,255,0.7);
    font-family: "Open Sans", Arial, sans-serif;
    font-size: 24px;
    color: var(--ink);
    display: flex;
    align-items: center;
    padding-left: 28px;
    box-sizing: border-box;
    white-space: nowrap;
  }
  .service-bar--promise { left: 40px; width: 440px; }
  .service-bar--services { left: 570px; width: 440px; }
</style>
</head>
<body>
  <section class="business-card">
    <svg class="grass-field" viewBox="0 0 1050 600" role="img" aria-label="Photograph of fresh green lawn grass rising across the card">
      <defs>
        <linearGradient id="grass-tone" x1="0" y1="0" x2="0" y2="1">
          <stop offset="0" stop-color="#9bcb3c"/>
          <stop offset="0.45" stop-color="#6fa83a"/>
          <stop offset="1" stop-color="#3f7a1f"/>
        </linearGradient>
      </defs>
      <path fill="url(#grass-tone)" d="M0 600 L0 520 C200 500 420 460 600 360 C720 290 790 150 830 0 L1050 0 L1050 600 Z"/>
    </svg>

    <div class="brand">
      <span class="brand-dot"></span>
      <span class="brand-name">Brantley Lawn Care</span>
    </div>

    <div class="contact">
      <h1 class="contact-name">Dexter Brantley</h1>
      <p class="contact-role">Lawn Care</p>
      <p class="contact-line">555-612-4470</p>
      <p class="contact-line">tidymow47@quillmail.example</p>
    </div>

    <div class="service-bar service-bar--promise">Fast, Friendly, quality service</div>
    <div class="service-bar service-bar--services">Trimming, Edging, Clean up</div>
  </section>
</body>
</html>
```